Donation Banner for Brookmere High School Entrances

Create a banner to be hung at entrances at the school, to encourage participation in donation campaign.

See examples on attached document. What I like about the sampes: clean, easy to read, clear, mission-oriented.

Brookmere Rd
Desired Size 100”w x 70”h

Corvell Rd Entrance
Desired Size 70”w x 50”h

Target Market(s)

Parents from the school and community members driving by. Silicon Valley professionals.

Font styles to use
Sans Serif

Colors
f78f20
9bcb3c
0393ce

Requirements
Must have
• School colors are orange and black. We can introduce small amounts of another color - maybe green to encourage donations. Or blue as it is opposite of orange on the color wheel.
• Banner must track dollar $$$ goal tracking up to $1.1M, in 200K increments (or whatever looks good) not %
• Our goal is 1.1M.
• Arrow Up, not thermometer.
• List website: bhsfundrise.org.
• Include round Brookmere Foundation logo, see file provided.
• Must include mission oriented messaging: Reduced Class Sizes, Expanded Electives, Student Support
• Our Organization is Brookmere High School Foundation, must be listed

```html
<!DOCTYPE html>
<html lang="en">
<head>
<meta charset="utf-8">
<title>Brookmere High School Foundation – Donation Banner</title>
<link rel="stylesheet" href="https://fonts.googleapis.com/css2?family=Anton&family=Oswald:wght@500;600;700&display=swap">
<style>
  :root {
    --orange: #f78f20;
    --orange-deep: #ec7a1c;
    --orange-light: #f9b04a;
    --cream: #fff6b8;
    --white: #ffffff;
    --ink: #3a2a12;
    --goal-red: #e4202e;
    --icon-fill: #f7a550;
  }
  * { margin: 0; padding: 0; box-sizing: border-box; }
  html, body { width: 1200px; height: 840px; overflow: hidden; background: var(--white); }

  .banner {
    position: relative;
    width: 1200px;
    height: 840px;
    overflow: hidden;
    background:
      radial-gradient(circle at 900px 360px, #fbc25e 0%, var(--orange-light) 25%, var(--orange) 60%, var(--orange-deep) 100%);
    font-family: "Oswald", "Arial Narrow", sans-serif;
  }

  .top-sweep { position: absolute; left: 0; top: 0; width: 1200px; height: 240px; }

  .foundation-seal {
    position: absolute;
    left: 510px; top: 8px;
    width: 188px; height: 188px;
    border-radius: 50%;
    background: var(--white);
    border: 4px solid var(--ink);
    display: flex; align-items: center; justify-content: center;
    text-align: center;
  }
  .foundation-name {
    font-family: "Oswald", sans-serif;
    font-weight: 600;
    font-size: 21px;
    line-height: 1.15;
    color: var(--ink);
    text-transform: uppercase;
    letter-spacing: 1px;
  }

  .headline {
    position: absolute;
    left: 30px; top: 288px;
    font-family: "Anton", "Impact", sans-serif;
    font-size: 64px;
    line-height: 1;
    color: var(--cream);
    letter-spacing: 0.5px;
    text-shadow: 3px 3px 0 #c45d0e;
  }

  .missions-title {
    position: absolute;
    left: 62px; top: 414px;
    width: 552px;
    display: flex; align-items: center; gap: 18px;
    color: var(--white);
    font-weight: 700;
    font-size: 30px;
    letter-spacing: 1px;
  }
  .missions-title::before, .missions-title::after {
    content: ""; flex: 1; height: 3px; background: var(--white);
  }

  .mission-list { position: absolute; left: 40px; top: 487px; display: flex; gap: 16px; }
  .mission { width: 180px; display: flex; flex-direction: column; align-items: center; }
  .mission-icon {
    width: 170px; height: 170px; border-radius: 50%;
    background: var(--white);
    display: flex; align-items: center; justify-content: center;
  }
  .mission-icon span { width: 104px; height: 104px; border-radius: 50%; background: var(--icon-fill); }
  .mission-label {
    margin-top: 10px;
    color: var(--white);
    font-weight: 500;
    font-size: 24px;
    white-space: nowrap;
  }

  .website { position: absolute; left: 70px; top: 748px; display: flex; align-items: center; gap: 22px; }
  .website-icon { width: 66px; height: 66px; border-radius: 50%; background: var(--white); }
  .website-url {
    font-family: "Anton", "Impact", sans-serif;
    font-size: 44px;
    color: var(--white);
    letter-spacing: 0.5px;
  }

  .goal-amount {
    position: absolute;
    left: 812px; top: 292px; width: 200px;
    text-align: center;
    font-family: "Anton", "Impact", sans-serif;
    font-size: 66px;
    line-height: 1;
    color: var(--cream);
    text-shadow: 3px 3px 0 #c45d0e;
  }

  .goal-arrow { position: absolute; left: 840px; top: 378px; width: 150px; height: 462px; }

  .milestone {
    position: absolute;
    font-family: "Oswald", sans-serif;
    font-weight: 700;
    color: var(--white);
    line-height: 1;
  }
  .milestone.left { right: 370px; text-align: right; }
  .milestone.right { left: 954px; }
  .m-880 { top: 470px; font-size: 34px; }
  .m-660 { top: 570px; font-size: 27px; }
  .m-440 { top: 672px; font-size: 23px; }
  .m-220 { top: 770px; font-size: 19px; }
</style>
</head>
<body>
<main class="banner">
  <svg class="top-sweep" viewBox="0 0 1200 240" aria-hidden="true">
    <path d="M0 0 H1200 V48 C1000 190 700 230 520 200 C330 170 150 120 0 86 Z" fill="#ffffff"/>
  </svg>

  <div class="foundation-seal">
    <p class="foundation-name">Brookmere<br>High School<br>Foundation</p>
  </div>

  <h1 class="headline">Help Us Reach Our Target</h1>

  <h2 class="missions-title">MISSIONS</h2>

  <ul class="mission-list">
    <li class="mission">
      <div class="mission-icon"><span role="img" aria-label="Icon of students seated at a desk"></span></div>
      <p class="mission-label">Reduced Class Sizes</p>
    </li>
    <li class="mission">
      <div class="mission-icon"><span role="img" aria-label="Icon of a stack of books"></span></div>
      <p class="mission-label">Expanded Electives</p>
    </li>
    <li class="mission">
      <div class="mission-icon"><span role="img" aria-label="Icon of a graduate held in supporting hands"></span></div>
      <p class="mission-label">Student Support</p>
    </li>
  </ul>

  <div class="website">
    <span class="website-icon" role="img" aria-label="Globe icon"></span>
    <p class="website-url">www.bhsfundrise.org</p>
  </div>

  <p class="goal-amount">$1.1M</p>

  <svg class="goal-arrow" viewBox="0 0 150 462" aria-hidden="true">
    <path d="M75 0 L142 66 H104 V462 H46 V66 H8 Z" fill="#ffffff"/>
    <rect x="54" y="308" width="42" height="154" fill="#e4202e"/>
  </svg>

  <span class="milestone left m-880">880K</span><span class="milestone right m-880">880K</span>
  <span class="milestone left m-660">660K</span><span class="milestone right m-660">660K</span>
  <span class="milestone left m-440">440K</span><span class="milestone right m-440">440K</span>
  <span class="milestone left m-220">220K</span><span class="milestone right m-220">220K</span>
</main>
</body>
</html>
```